Creative label for amber glass candle jar.

We are a candle company. Our products are handmade by us and natural. We are looking for something minimalistic and unique. We need a label for our candle jars (amber glass with black lid). Our current label doesn't match these requirements. We would like our products to be stocked in London shop, therefore design has to be up to a high standard. Jar specification Diameter (mm) 65 Height without cap (mm) 80. We want the new design to be different from the current one. It's just a guide for wording.
We should be able adjust the label, to change scent name.
Our scents are
*Coconut & Vanilla
*Lavender
*Bergamot
*Italian Garden
*Hygge
*Eucalyptus & Peppermint
*Coffee
*Cedarwood & Juniperberry
To know more about us, visit our website www.fenwickbrae.com or instagram.com/fenwickbrae
Good luck!
Industry/Entity Type
It Company
Colors
Designer to choose colors to be used in the design.
Requirements
Must have
- * I have attached two of our logos, label design must include one of them.
- *has to mention that it's made in London
- *has to say that candle is natural/made with essential oils
- *has to have scent name and No. on it..
- Label can be vertical or horizontal, but has to be square/rectangular,.
Should not have
- Label should not be round

```html
<!DOCTYPE html>
<html lang="en">
<head>
<meta charset="utf-8">
<title>Fenwick Brae – Natural Candle Labels</title>
<link href="https://fonts.googleapis.com/css2?family=Raleway:ital,wght@0,400;0,500;0,700;1,400&display=swap" rel="stylesheet">
<style>
  :root {
    --page: #ffffff;
    --label: #ffffff;
    --frame: #9a9a9a;
    --ink: #1a1a1a;
    --ink-soft: #444444;
    --seal: #b9b9b9;
    --band-coconut: #c8b68e;
    --band-lavender: #dab6d0;
    --band-bergamot: #abc56c;
    --band-garden: #a8aaac;
  }
  * { box-sizing: border-box; margin: 0; padding: 0; }
  html, body {
    width: 1200px; height: 867px; overflow: hidden;
    background: var(--page);
    font-family: "Raleway", sans-serif;
    color: var(--ink);
  }
  .range {
    position: absolute; left: 0; top: 0;
    width: 1200px; height: 867px;
    display: flex; justify-content: center; align-items: center;
    gap: 60px;
  }
  .label {
    width: 210px; height: 275px;
    background: var(--label);
    padding: 8px;
    box-shadow: 0 1px 4px rgba(0,0,0,0.18);
  }
  .label__frame {
    position: relative;
    width: 100%; height: 100%;
    border: 1.5px solid var(--frame);
    padding: 5px;
    display: flex; flex-direction: column; align-items: center;
  }
  .label__band {
    width: 100%; height: 44px;
    display: flex; align-items: center; justify-content: center;
  }
  .label__brand {
    font-size: 21px; font-weight: 500;
    letter-spacing: 3px; text-transform: lowercase;
    color: var(--ink);
    white-space: nowrap;
  }
  .band--coconut { background: var(--band-coconut); }
  .band--lavender { background: var(--band-lavender); }
  .band--bergamot { background: var(--band-bergamot); }
  .band--garden { background: var(--band-garden); }
  .label__scent {
    height: 74px;
    display: flex; align-items: center; justify-content: center;
    text-align: center;
    font-size: 22px; font-weight: 700; line-height: 1.12;
    text-transform: uppercase; letter-spacing: 0.5px;
  }
  .label__type {
    margin-top: 10px;
    border: 1px solid var(--ink-soft);
    padding: 1px 6px;
    font-size: 12.5px; color: var(--ink-soft);
  }
  .label__oils {
    margin-top: 8px;
    font-size: 11.5px; font-style: italic; color: var(--ink-soft);
  }
  .label__foot {
    position: absolute; left: 12px; right: 8px; bottom: 8px;
    display: flex; align-items: center;
  }
  .label__origin {
    font-size: 11.5px; font-style: italic; color: var(--ink-soft);
    flex: 1;
  }
  .label__seal {
    width: 38px; height: 38px; border-radius: 50%;
    border: 1.5px solid var(--seal);
  }
</style>
</head>
<body>
<main class="range">

  <article class="label">
    <div class="label__frame">
      <div class="label__band band--coconut"><span class="label__brand">fenwick brae</span></div>
      <h2 class="label__scent">Coconut<br>&amp; Vanilla</h2>
      <p class="label__type">Natural Candle</p>
      <p class="label__oils">Made With Essential Oils</p>
      <div class="label__foot">
        <span class="label__origin">Made in London</span>
        <span class="label__seal"></span>
      </div>
    </div>
  </article>

  <article class="label">
    <div class="label__frame">
      <div class="label__band band--lavender"><span class="label__brand">fenwick brae</span></div>
      <h2 class="label__scent">Lavender</h2>
      <p class="label__type">Natural Candle</p>
      <p class="label__oils">Made With Essential Oils</p>
      <div class="label__foot">
        <span class="label__origin">Made in London</span>
        <span class="label__seal"></span>
      </div>
    </div>
  </article>

  <article class="label">
    <div class="label__frame">
      <div class="label__band band--bergamot"><span class="label__brand">fenwick brae</span></div>
      <h2 class="label__scent">Bergamot</h2>
      <p class="label__type">Natural Candle</p>
      <p class="label__oils">Made With Essential Oils</p>
      <div class="label__foot">
        <span class="label__origin">Made in London</span>
        <span class="label__seal"></span>
      </div>
    </div>
  </article>

  <article class="label">
    <div class="label__frame">
      <div class="label__band band--garden"><span class="label__brand">fenwick brae</span></div>
      <h2 class="label__scent">Italian<br>Garden</h2>
      <p class="label__type">Natural Candle</p>
      <p class="label__oils">Made With Essential Oils</p>
      <div class="label__foot">
        <span class="label__origin">Made in London</span>
        <span class="label__seal"></span>
      </div>
    </div>
  </article>

</main>
</body>
</html>
```